Business Card Design Project

Please create a custom business card for Plume analytics. The logo is attached to this brief.

Address :
CEO : Baptiste Lorand
Mobile : +33641927508
14 rue Véronèse
75013 Paris
France

Reason: Sorry wrong logo. I will update asap

Hi, Sorry, I post the wrong file. I just update the correct logo. If you can integrate some charts as background it will be nice

Hi Everybody Please make it beautifull, clean, soft like pebble designs does to create their product. I want somewhere to show in a beautifull way some datavisualization charts. Not to much, but try to find a way to design it beautifull with less. Get inspire by datavisualization : http://www.morvelkit.com/48207-clean-vector-infographic-and-data-visualization-design-elements-03/

Target Market(s)

B to B
Customers are accountant, CPA, finance departement

Industry/Entity Type

Business

Font styles to use
Sans Serif

Requirements
Must have
• I want to give a clear message about what we do. We do dashboards, we create beautifull charts
Nice to have
• displays charts icons to let people know tha we do charts

```html
<!DOCTYPE html>
<html lang="en">
<head>
<meta charset="utf-8">
<title>Plume analytics – Business Card</title>
<link rel="stylesheet" href="https://fonts.googleapis.com/css2?family=Alegreya+Sans:wght@400;500&display=swap">
<style>
  :root {
    --stage: #2b1c18;
    --paper: #ffffff;
    --sky: #42aef0;
    --amber: #f6b31f;
    --slate: #3f4649;
    --ink: #3a3f42;
    --link-blue: #1f6fc6;
  }
  * { box-sizing: border-box; margin: 0; padding: 0; }
  html, body {
    width: 1200px; height: 1000px; overflow: hidden;
    background: var(--stage);
    font-family: "Alegreya Sans", sans-serif;
  }
  .canvas { position: relative; width: 1200px; height: 1000px; }
  .card {
    position: absolute; left: 276px; width: 698px; height: 400px;
    background: var(--paper); overflow: hidden;
  }
  .card--front { top: 70px; }
  .card--back { top: 544px; }

  .rule { position: absolute; left: 0; right: 0; height: 3px; }
  .rule--top { top: 61px; background: var(--sky); }
  .rule--bottom { top: 333px; background: var(--amber); }

  .band { position: absolute; top: 172px; height: 58px; background: var(--sky); }
  .band--left { left: 0; width: 152px; }
  .band--right { left: 536px; right: 0; }

  .brand {
    position: absolute; left: 172px; top: 168px; width: 346px; height: 66px;
    display: flex; align-items: center; gap: 14px;
  }
  .brand__mark { width: 44px; height: 44px; background: var(--sky); flex: none; }
  .brand__name {
    font-size: 40px; font-weight: 400; color: var(--ink); white-space: nowrap;
  }

  .tag {
    position: absolute; display: flex; align-items: center;
    font-weight: 500; letter-spacing: 2px; white-space: nowrap;
  }
  .tag--role {
    left: 0; top: 54px; width: 405px; height: 58px; padding-left: 44px;
    background: var(--sky); color: #fff; font-size: 32px;
  }
  .tag--mobile {
    left: 254px; top: 161px; right: 0; height: 58px; padding-left: 20px;
    background: var(--amber); color: var(--ink); font-size: 32px;
  }
  .tag--mobile .tag__value { color: var(--link-blue); margin-left: 10px; }
  .tag--address {
    left: 69px; top: 274px; width: 569px; height: 73px;
    flex-direction: column; align-items: flex-start; justify-content: center;
    padding-left: 12px; line-height: 28px;
    background: var(--slate); color: #fff; font-size: 29px;
    box-shadow: 0 2px 8px rgba(0,0,0,.35);
  }
  .tag--address .tag__line2 { padding-left: 128px; }
</style>
</head>
<body>
<main class="canvas">
  <section class="card card--front" aria-label="Card front">
    <div class="rule rule--top"></div>
    <div class="band band--left"></div>
    <div class="band band--right"></div>
    <div class="brand">
      <span class="brand__mark"></span>
      <span class="brand__name">Plume analytics</span>
    </div>
    <div class="rule rule--bottom"></div>
  </section>

  <section class="card card--back" aria-label="Card back">
    <p class="tag tag--role">CEO : Baptiste Lorand</p>
    <p class="tag tag--mobile">Mobile :<span class="tag__value">+336.41.92.75.08</span></p>
    <address class="tag tag--address" style="font-style:normal">
      <span>Address : 14 rue Véronèse, 75013 Paris</span>
      <span class="tag__line2">France</span>
    </address>
  </section>
</main>
</body>
</html>
```